Business Card Design

Marla Quibbet
Artist of Contemporary/Modern/Representational Art
Contact: 0457219308
Please include my web site (thanks)! http://www.artvault913.com.au/marla-quibbet
And
Email: marlaquibbet@fernpost.example

Target Market(s)

Modern professional People who know what they like in modern contemporary art and have the means to purchase it.

Industry/Entity Type

Business

Contact Information for Business Card

Marla Quibbet
Contact: 0457219308

Font styles to use
Sans Serif

Requirements
Must have
• Simplicity & to the point
Keep the font modern/ contemporary
Nice to have
• A portrait of me and one piece of work on the business card (one on each side).
Should not have
• I'm not into butterflies.
No feminine style swirls
Nor I like swirls that look like tatoos

```html
<!DOCTYPE html>
<html lang="en">
<head>
<meta charset="utf-8">
<title>Marla Quibbet – Business Card</title>
<link rel="stylesheet" href="https://fonts.googleapis.com/css2?family=Quicksand:wght@600;700&display=swap">
<style>
  :root {
    --page-bg: #2b2b2d;
    --card-green: #8fc741;
    --card-green-light: #a3d35a;
    --ink: #3a3b2c;
    --river-blue: #2f7fb0;
    --sky-blue: #3d5f9e;
    --city-tone-a: #5a8a9c;
    --city-tone-b: #6b8d4a;
    --house-red: #c8342c;
    --house-yellow: #f0d23a;
    --house-green: #9cb86a;
  }
  html, body {
    margin: 0;
    width: 1200px;
    height: 849px;
    overflow: hidden;
    background: var(--page-bg);
  }
  .card {
    position: absolute;
    left: 150px;
    top: 174px;
    width: 900px;
    height: 500px;
    border-radius: 26px;
    overflow: hidden;
    background: linear-gradient(180deg, var(--card-green-light), var(--card-green));
    font-family: "Quicksand", sans-serif;
    color: var(--ink);
  }
  .artwork-city {
    position: absolute;
    left: 0; top: 0;
    width: 440px; height: 236px;
    background: linear-gradient(160deg, #9ec3d6 0%, var(--city-tone-a) 30%, var(--river-blue) 50%, var(--city-tone-b) 75%, #7a9a5a 100%);
  }
  .artwork-houses {
    position: absolute;
    left: 440px; top: 0;
    width: 460px; height: 236px;
    background:
      linear-gradient(180deg, var(--sky-blue) 0%, #5a78b4 30%, transparent 30%),
      linear-gradient(90deg, var(--house-red) 0%, var(--house-red) 20%, var(--house-green) 20%, var(--house-green) 38%, var(--house-red) 38%, #d27a3a 56%, var(--house-yellow) 56%, var(--house-yellow) 76%, var(--house-green) 76%);
  }
  .accent-strip {
    position: absolute;
    left: 0; top: 236px;
    width: 900px; height: 5px;
    background: linear-gradient(90deg, #d84a3a, #f0d23a, #4a8ac8, #d84a3a, #6aa84a, #f0d23a, #4a8ac8);
  }
  .accent-band {
    position: absolute;
    left: 0; top: 241px;
    width: 440px; height: 9px;
    background: var(--river-blue);
  }
  .details {
    position: absolute;
    left: 0; top: 258px;
    width: 900px;
    text-align: center;
  }
  .name {
    margin: 0;
    font-size: 40px;
    font-weight: 700;
    letter-spacing: 0.5px;
    line-height: 1.2;
  }
  .title {
    margin: 8px 0 0;
    font-size: 18px;
    font-weight: 700;
  }
  .contact-line {
    margin: 12px 0 0;
    font-size: 18px;
    font-weight: 700;
    display: flex;
    align-items: center;
    justify-content: center;
    gap: 10px;
  }
  .contact-line svg { width: 18px; height: 18px; flex: none; }
</style>
</head>
<body>
  <div class="card">
    <div class="artwork-city" role="img" aria-label="Painting of a city with a winding river and stadiums"></div>
    <div class="artwork-houses" role="img" aria-label="Painting of a row of colourful gabled townhouses"></div>
    <div class="accent-strip"></div>
    <div class="accent-band"></div>

    <div class="details">
      <h1 class="name">Marla Quibbet</h1>
      <p class="title">Artist of Contemporary/Modern/Representational Art</p>
      <p class="contact-line">
        <svg viewBox="0 0 20 20" aria-hidden="true"><circle cx="10" cy="10" r="8.5" fill="none" stroke="currentColor" stroke-width="1.6"/><circle cx="10" cy="10" r="4" fill="none" stroke="currentColor" stroke-width="1.6"/></svg>
        http://www.artvault913.com.au/marla-quibbet
      </p>
      <p class="contact-line">
        <svg viewBox="0 0 20 20" aria-hidden="true"><circle cx="10" cy="10" r="8.5" fill="none" stroke="currentColor" stroke-width="1.6"/><path d="M7 6.5c0 4 2.5 6.8 6.5 7l0.8-1.8-2-1-1 1c-1.2-.6-2.2-1.6-2.8-2.8l1-1-1-2z" fill="currentColor"/></svg>
        0457219308
      </p>
      <p class="contact-line">
        <svg viewBox="0 0 20 20" aria-hidden="true"><circle cx="10" cy="10" r="8.5" fill="none" stroke="currentColor" stroke-width="1.6"/><rect x="5.5" y="7" width="9" height="6.5" fill="none" stroke="currentColor" stroke-width="1.3"/><path d="M5.5 7l4.5 3.6L14.5 7" fill="none" stroke="currentColor" stroke-width="1.3"/></svg>
        marlaquibbet@fernpost.example
      </p>
    </div>
  </div>
</body>
</html>
```